Trevolar bonds (Surety bond broker)

We are a broker of surety bonds, we need a presentation and a flyer with fresh design. Our core values are reliable, on time and customized service. We want to transmit to our clients, they can leave on us the process of underwriting and issuing a surety bond, so they can focus on their business with no distractions.

Font styles to use
Sans Serif
Other font styles liked:
• view logos

Requirements
Must have
• Visually attractive.
Main Message: Fast service issuing and underwriting surety bonds, reliable, nos surprises, we are always one step ahead, customized and personalized bonding solutions.
Nice to have
• Have short version for the flyer, and extended version for the presentation.
Should not have
• We already have a logo (attached), maintain colors

```html
<!DOCTYPE html>
<html lang="es">
<head>
<meta charset="utf-8">
<title>Trevolar bonds – Folleto</title>
<link rel="stylesheet" href="https://fonts.googleapis.com/css2?family=Montserrat:wght@400;500;600;700;800&display=swap">
<style>
  :root{
    --ink:#0a0a0a;
    --paper:#ececec;
    --green:#6aa43a;
    --green-dark:#5b9230;
    --white:#ffffff;
    --muted:#d9d9d9;
    --text-dark:#2a2a2a;
  }
  *{box-sizing:border-box;margin:0;padding:0}
  html,body{width:1200px;height:800px;overflow:hidden;background:#f4f4f4}
  body{font-family:"Montserrat",Arial,sans-serif}
  .brochure{display:flex;width:1200px;height:800px}
  .panel{position:relative;width:400px;height:800px;overflow:hidden}
  .panel--dark{background:var(--ink);color:var(--white)}
  .panel--light{background:var(--paper);color:var(--text-dark)}
  .panel--dark + .panel--dark{border-left:1px solid #222}

  .heading{font-size:25px;font-weight:600;letter-spacing:.2px;line-height:1.2}
  .heading .accent{color:var(--green)}
  .dash{display:block;width:22px;height:3px;background:currentColor;margin:12px 0 16px}
  .panel--light .dash{background:var(--ink)}
  .hl{color:var(--green);font-weight:700}

  /* panel 1 */
  .value{position:absolute;left:38px;top:52px;width:330px}
  .value p{font-size:11.5px;line-height:1.45;margin-bottom:12px;color:var(--muted)}
  .services{position:absolute;left:38px;top:470px;width:340px}
  .service-list{list-style:none}
  .service-list li{position:relative;padding-left:22px;font-size:13px;font-weight:600;line-height:1.3;margin-bottom:9px}
  .service-list li::before{content:"✓";position:absolute;left:0;top:0;color:var(--green);font-weight:700}
  .service-list small{display:block;font-size:8.5px;font-weight:400;color:#bbb}

  /* panel 2 */
  .products-title{position:absolute;left:34px;top:52px}
  .connectors{position:absolute;inset:0;pointer-events:none}
  .bond{position:absolute;width:112px;height:112px;border-radius:50%;background:var(--green);
    box-shadow:0 0 0 3px var(--green),inset 0 0 0 3px var(--ink),inset 0 0 0 5px var(--white);
    display:flex;flex-direction:column;align-items:center;justify-content:center;gap:8px}
  .bond__icon{width:38px;height:38px;border-radius:50%;background:#8cc25c}
  .bond__label{font-size:11px;font-weight:600;color:var(--white)}
  .bond-list{position:absolute;list-style:none;font-size:10.5px;line-height:15px;color:var(--muted)}
  .bond-list .tick{color:var(--green);font-weight:600}
  .bond-list .tick::before{content:"✓ ";color:var(--white)}
  .bond-list .dot{padding-left:12px;position:relative}
  .bond-list .dot::before{content:"";position:absolute;left:2px;top:6px;width:4px;height:4px;border-radius:50%;background:var(--white)}

  /* panel 3 */
  .special{position:absolute;left:36px;top:52px;width:330px}
  .special .heading{color:var(--ink)}
  .special-item{margin-bottom:20px}
  .special-item h3{font-size:14.5px;font-weight:600;color:var(--green);margin-bottom:6px;line-height:1.25}
  .special-item p{font-size:11px;line-height:1.5;color:#444}
  .cta{position:absolute;left:0;top:640px;width:360px}
  .cta__band{background:var(--green);color:var(--white);font-size:34px;font-weight:800;letter-spacing:1px;padding:8px 0 8px 36px}
  .cta__phone{font-size:36px;font-weight:800;color:var(--ink);padding:8px 0 0 36px;letter-spacing:.5px}
</style>
</head>
<body>
<main class="brochure">

  <section class="panel panel--dark">
    <div class="value">
      <h2 class="heading">Nuestra oferta <span class="accent">de valor</span></h2>
      <span class="dash"></span>
      <p><span class="hl">Para nuestros fiados,</span> nos aseguramos de que el proceso de emisión de fianzas sea <span class="hl">claro, rápido y sencillo.</span> Dando una asesoría personalizada y seguimiento puntual a cada solicitud.</p>
      <p>Sabemos la importancia de tener una fianza en tiempo y sin errores, por lo que nos empeñamos en siempre ir un paso adelante, permitiendo que nuestros clientes se despreocupen del proceso de afianzamiento y logren todos sus objetivos.</p>
      <p><span class="hl">Para nuestros beneficiarios,</span> trabajamos solo con las mejores afianzadoras del país y garantizamos que todos nuestros clientes cuenten con una garantía confiable, que les permita concluir sus proyectos con la tranquilidad de que tienen un respaldo confiable. Nuestro compromiso es siempre mitigar los riesgos y nunca dejar desprotegidos a nuestros clientes.</p>
    </div>
    <div class="services">
      <h2 class="heading">Nuestros <span class="accent">Servicios</span></h2>
      <span class="dash"></span>
      <ul class="service-list">
        <li>Asesoría personalizada para la obtención de Líneas de Afianzamiento</li>
        <li>Emisión y administración de fianzas.<small>(Fidelidad, Administrativas, Judiciales, Crédito y Fideicomisos)</small></li>
        <li>Diseño, implementación y gestión de esquemas de afianzamiento.</li>
        <li>Asesoría en riesgos para contratos de obra, suministro y proveeduría.</li>
        <li>Colocación de fianzas internacionales y reaseguro.</li>
        <li>Asesoría legal en proceso de reclamación de fianzas.</li>
        <li>Esquemas de afianzamiento masivos.</li>
      </ul>
    </div>
  </section>

  <section class="panel panel--dark">
    <div class="products-title">
      <h2 class="heading">Productos en <span class="accent">Fianzas</span></h2>
      <span class="dash"></span>
    </div>

    <svg class="connectors" viewBox="0 0 400 800" aria-hidden="true">
      <g fill="none" stroke="#fff" stroke-width="1">
        <polyline points="140,190 160,175 280,165"/>
        <polyline points="150,400 150,420 300,390"/>
        <polyline points="185,575 185,600 340,575"/>
        <polyline points="215,745 215,770 375,745"/>
      </g>
      <g fill="#6aa43a">
        <circle cx="280" cy="165" r="2.5"/><circle cx="300" cy="390" r="2.5"/>
        <circle cx="340" cy="575" r="2.5"/><circle cx="375" cy="745" r="2.5"/>
      </g>
    </svg>

    <div class="bond" style="left:30px;top:130px">
      <span class="bond__icon" role="img" aria-label="Icono de fidelidad"></span>
      <span class="bond__label">Fidelidad</span>
    </div>
    <ul class="bond-list" style="left:175px;top:130px">
      <li class="tick">Colectiva</li>
      <li class="tick">Individual</li>
    </ul>

    <div class="bond" style="left:60px;top:295px">
      <span class="bond__icon" role="img" aria-label="Icono de mazo judicial"></span>
      <span class="bond__label">Judicial</span>
    </div>
    <ul class="bond-list" style="left:190px;top:235px">
      <li class="tick">Penales</li>
      <li class="dot">Libertad provisional</li>
      <li class="dot">Condena provisional</li>
      <li class="dot">Reparación del daño</li>
      <li class="dot">Sanción pecuniaria</li>
      <li class="tick">No Penales</li>
      <li class="dot">Daños y prejuicios</li>
      <li class="dot">Pensión alimenticia</li>
      <li class="dot">Laboral</li>
    </ul>

    <div class="bond" style="left:95px;top:465px">
      <span class="bond__icon" role="img" aria-label="Icono de persona aprobada"></span>
      <span class="bond__label">Administrativas</span>
    </div>
    <ul class="bond-list" style="left:222px;top:438px">
      <li class="tick">Obra y Proveeduría</li>
      <li class="dot">Cumplimiento</li>
      <li class="dot">Anticipo</li>
      <li class="dot">Buena Calidad</li>
      <li class="dot">Contingencias Laborales</li>
      <li class="tick">Arrendamiento</li>
      <li class="tick">Contingencias ambientales</li>
      <li class="tick">Fiscales</li>
    </ul>

    <div class="bond" style="left:125px;top:635px">
      <span class="bond__icon" role="img" aria-label="Icono de tarjetas de crédito"></span>
      <span class="bond__label">Crédito</span>
    </div>
    <ul class="bond-list" style="left:252px;top:620px">
      <li class="tick">Compra venta</li>
      <li class="tick">Suministro</li>
      <li class="dot">CEN</li>
      <li class="dot">Estaciones de Servicio</li>
      <li class="dot">PETRONAL</li>
      <li class="dot">AERONAL</li>
      <li class="tick">Otras Crédito</li>
    </ul>
  </section>

  <section class="panel panel--light">
    <div class="special">
      <h2 class="heading">Productos <span class="accent">Especiales</span></h2>
      <span class="dash"></span>
      <div class="special-item">
        <h3>Flujo Garantizado</h3>
        <p>Es una fianza con la que se constituye un fondo colectivo para productos masivos que permite darle viabilidad financiera a tu empresa, proporcionándole el flujo constante de recursos para cubrir posibles pérdidas por quebrantos de créditos o cuentas por cobrar no liquidadas por sus clientes.</p>
      </div>
      <div class="special-item">
        <h3>Esquemas de Proveedores</h3>
        <p>Esquema diseñado para grandes beneficiarios, que permite proteger los recursos invertidos en proyectos de construcción y adquisición de bienes o prestación de servicios, garantizando las obligaciones que se derivan de estos a cargo de sus proveedores o contratistas.</p>
        <p style="margin-top:10px">Este programa permite la fácil administración de fianzas, previniendo un procedimiento ágil para la ejecución y cobro de las garantías que se emitan dentro del esquema.</p>
      </div>
      <div class="special-item">
        <h3>Programa de<br>garantías de fianzas para PyMEs</h3>
        <p>Con este programa puedes incrementar la línea de afianzamiento, gracias a que Fondenal aporta 50% de las garantías requeridas en fianzas hasta por 30 millones de pesos</p>
      </div>
    </div>
    <div class="cta">
      <div class="cta__band">CALL FOR INFO</div>
      <div class="cta__phone">+52 55 3100 2750</div>
    </div>
  </section>

</main>
</body>
</html>
```